Redesign of business card for Birchline Mechanical

We are looking for a new design for our business cards for Birchline Mechanical. We are a plumbing & HVAC construction company, operating on the West Coast of Canada and USA. Logo attached.
Industry/Entity Type
Construction - Plumbing & HVAC
Contact Information for Business Card
Name, address, phone numbers, email, website address
Look and feel
Each slider illustrates characteristics of the customer's brand and the style your logo design should communicate.

```html
<!DOCTYPE html>
<html lang="en">
<head>
<meta charset="utf-8">
<title>Birchline Mechanical — Business Card</title>
<link rel="stylesheet" href="https://fonts.googleapis.com/css2?family=Montserrat:wght@400;500;700&family=Oswald:wght@500&display=swap">
<style>
  :root {
    --canvas: #3a3a3c;
    --card-white: #ffffff;
    --card-black: #1c1c1d;
    --ink: #1f1f20;
    --ink-soft: #2e2e30;
    --silver: #c9c9cb;
    --edge-grey: #b9b9bb;
  }
  * { margin: 0; padding: 0; box-sizing: border-box; }
  html, body {
    width: 1200px; height: 1200px; overflow: hidden;
    background: var(--canvas);
  }
  .stage { position: relative; width: 1200px; height: 1200px; }

  .card {
    position: absolute; left: 180px;
    width: 840px; height: 480px;
    border-radius: 44px; overflow: hidden;
  }

  /* Front */
  .card--front { top: 90px; background: var(--card-white); }
  .front__band {
    position: absolute; left: 0; right: 0; bottom: 0; height: 22px;
    background: linear-gradient(100deg, var(--ink) 0 60%, var(--card-white) 60% 61.2%, var(--edge-grey) 61.2% 100%);
  }
  .holder {
    position: absolute; left: 64px; top: 200px;
    font-family: "Montserrat", sans-serif; color: var(--ink);
  }
  .holder__name { font-size: 46px; font-weight: 700; letter-spacing: 1px; line-height: 1; }
  .holder__role { font-size: 26px; font-weight: 500; letter-spacing: 1px; margin-top: 4px; }
  .contact { list-style: none; margin-top: 14px; }
  .contact__item {
    display: flex; align-items: flex-start; gap: 12px;
    font-size: 21px; line-height: 28px; color: var(--ink-soft);
  }
  .contact__icon { width: 20px; height: 20px; margin-top: 4px; flex: none; fill: var(--ink); }

  .wordmark {
    position: absolute; display: flex; align-items: center; gap: 18px;
    font-family: "Oswald", sans-serif; font-weight: 500;
    text-transform: uppercase; letter-spacing: 2px; line-height: 1.05;
  }
  .wordmark__square { flex: none; border-radius: 6px; }
  .card--front .wordmark { right: 70px; top: 120px; color: var(--ink); font-size: 38px; }
  .card--front .wordmark__square { width: 64px; height: 64px; border: 7px solid var(--ink); }

  /* Back */
  .card--back { top: 630px; background: var(--card-black); }
  .card--back .wordmark {
    left: 50%; top: 50%; transform: translate(-50%, -50%);
    color: var(--silver); font-size: 52px; white-space: nowrap;
  }
  .card--back .wordmark__square { width: 86px; height: 86px; border: 9px solid var(--silver); }
</style>
</head>
<body>
<main class="stage">

  <section class="card card--front" aria-label="Business card front">
    <div class="wordmark">
      <span class="wordmark__square"></span>
      <span class="wordmark__name">Birchline<br>Mechanical</span>
    </div>

    <div class="holder">
      <p class="holder__name">FULL NAME</p>
      <p class="holder__role">POSITION</p>
      <ul class="contact">
        <li class="contact__item">
          <svg class="contact__icon" viewBox="0 0 24 24"><path d="M6.6 10.8a15.1 15.1 0 0 0 6.6 6.6l2.2-2.2c.3-.3.7-.4 1-.2 1.1.4 2.3.6 3.6.6.6 0 1 .4 1 1V20c0 .6-.4 1-1 1A17 17 0 0 1 3 4c0-.6.4-1 1-1h3.5c.6 0 1 .4 1 1 0 1.3.2 2.5.6 3.6.1.3 0 .7-.2 1z"/></svg>
          <span>(000) 000 0000</span>
        </li>
        <li class="contact__item">
          <svg class="contact__icon" viewBox="0 0 24 24"><path d="M2 5h20v14H2z M3.5 6.5 12 13l8.5-6.5" fill="none" stroke="#1f1f20" stroke-width="2"/></svg>
          <span>email@company.com</span>
        </li>
        <li class="contact__item">
          <svg class="contact__icon" viewBox="0 0 24 24" fill="none" stroke="#1f1f20" stroke-width="1.8"><circle cx="12" cy="12" r="9"/><ellipse cx="12" cy="12" rx="4" ry="9"/><path d="M3 12h18M4.5 7.5h15M4.5 16.5h15"/></svg>
          <span>www.company.com</span>
        </li>
        <li class="contact__item">
          <svg class="contact__icon" viewBox="0 0 24 24"><path d="M12 2a7 7 0 0 0-7 7c0 5.2 7 13 7 13s7-7.8 7-13a7 7 0 0 0-7-7zm0 9.5A2.5 2.5 0 1 1 12 6.5a2.5 2.5 0 0 1 0 5z"/></svg>
          <span>123 Name Street, 000<br>Your City, 00000-000</span>
        </li>
      </ul>
    </div>

    <div class="front__band"></div>
  </section>

  <section class="card card--back" aria-label="Business card back">
    <div class="wordmark">
      <span class="wordmark__square"></span>
      <span class="wordmark__name">Birchline<br>Mechanical</span>
    </div>
  </section>

</main>
</body>
</html>
```